Silver Lumen Med Spa Membership Sales Presentation to Clients handout

Hello! We are a high tech, Silver Lumen Med Spa in Dallas Texas that won Best Med Spa in Addison. I want my graphic membership form to represent that. We serve women and men so want it neutral but show cutting edge. Our colors are black, white, gray but would entertain your view. Having a challenge on making it easy to read as each membership gets more services yet one service a month. Thought maybe colorcoding what services are together? Definite road blocks on my end. I used Canva to lay out, but as you can see I am NOT gifted at graphic design. ;))

Target Market(s)

39-69

Industry/Entity Type

Medical Med Spa

Requirements
Must have
• cutting edge look

```html
<!DOCTYPE html>
<html lang="en">
<head>
<meta charset="utf-8">
<title>Silver Lumen Med Spa – Ageless Glow Memberships</title>
<link href="https://fonts.googleapis.com/css2?family=Montserrat:wght@400;600;700&display=swap" rel="stylesheet">
<style>
  :root{
    --backdrop:#0b2753;
    --paper:#ffffff;
    --ink:#111111;
    --band-gray:#a6a6a6;
    --wash:#f3f3f3;
    --dot:#b5b5b5;
    --badge-ring:#2b4a86;
  }
  *{margin:0;padding:0;box-sizing:border-box}
  html,body{width:1200px;height:1200px;overflow:hidden;background:var(--backdrop)}
  body{position:relative;font-family:"Montserrat",Arial,sans-serif;color:var(--ink)}
  .sheet{position:absolute;left:207px;top:49px;width:786px;height:1101px;background:var(--paper);overflow:hidden}
  .sheet-art{position:absolute;inset:0}
  .brand{position:absolute;left:26px;top:74px;display:flex;align-items:center;gap:8px}
  .brand-dot{width:16px;height:16px;border-radius:50%;background:var(--ink);flex:none}
  .brand-name{font-weight:600;font-size:14px;line-height:18px;color:var(--ink);white-space:nowrap}
  .title{position:absolute;right:25px;top:54px;text-align:right;color:var(--paper);font-weight:700;font-variant:small-caps;font-size:45px;line-height:52px;letter-spacing:1px}
  .title .line-two{font-size:52px}
  .col-head{position:absolute;top:169px;height:27px;line-height:27px;color:var(--paper);font-weight:700;font-size:22px}
  .col-head.treatments{left:37px}
  .col-head.tier{width:110px;text-align:center}
  .price-row{position:absolute;left:0;top:204px;width:786px;height:45px;color:var(--paper);font-weight:700}
  .price-row .label{position:absolute;left:37px;top:4px;font-size:15.5px;line-height:19px}
  .price-row .price{position:absolute;top:0;width:110px;height:45px;line-height:45px;text-align:center;font-size:16px}
  .good{left:361px}.better{left:507px}.best{left:649px}
  .row{position:absolute;left:0;width:786px;height:26px;font-size:14.6px;line-height:26px}
  .row::after{content:"";position:absolute;left:23px;right:24px;top:25px;border-bottom:1.5px dotted var(--dot)}
  .row.end::after{display:none}
  .row .name{position:absolute;left:37px}
  .row .cell{position:absolute;top:0;width:110px;height:26px;text-align:center;display:flex;align-items:center;justify-content:center}
  .row .cell svg{width:17px;height:17px}
  .footer-item{position:absolute;top:1059px;height:22px;display:flex;align-items:center;gap:8px;font-size:13.5px;color:var(--paper)}
  .footer-item svg{width:19px;height:19px}
  .footer-item.web{left:39px;color:#f2f2f2}
  .footer-item.phone{left:300px}
  .footer-item.place{left:502px}
</style>
</head>
<body>
<svg width="0" height="0" style="position:absolute">
  <symbol id="tick" viewBox="0 0 20 20">
    <circle cx="10" cy="10" r="10" fill="#111"/>
    <path d="M5.3 10.4l3.1 3.1 6.4-6.8" fill="none" stroke="#fff" stroke-width="2.4" stroke-linecap="round" stroke-linejoin="round"/>
  </symbol>
</svg>

<main class="sheet">
  <svg class="sheet-art" viewBox="0 0 786 1101" width="786" height="1101">
    <polygon fill="var(--wash)" points="265,249 687,249 178,1055 0,1055 0,634"/>
    <polygon fill="var(--band-gray)" points="305,131 334,69 390,69 361,131"/>
    <polygon fill="var(--ink)" points="399,40 786,40 786,157 324,157"/>
    <rect x="0" y="156" width="330" height="1.5" fill="var(--ink)"/>
    <circle cx="222" cy="92" r="56" fill="#111" stroke="var(--badge-ring)" stroke-width="2"/>
    <rect x="0" y="169" width="786" height="27" fill="var(--band-gray)"/>
    <polygon fill="var(--paper)" points="356,169 366,169 344,196 334,196"/>
    <polygon fill="var(--paper)" points="495,169 505,169 492,196 482,196"/>
    <polygon fill="var(--paper)" points="645,169 655,169 642,196 632,196"/>
    <polygon fill="#e4e4e4" points="760,169 786,169 786,196 743,196"/>
    <rect x="0" y="204" width="786" height="45" fill="var(--ink)"/>
    <g fill="var(--ink)">
      <rect x="23" y="352.3" width="739" height="2"/>
      <rect x="23" y="459.2" width="739" height="2"/>
      <rect x="23" y="488.3" width="739" height="2"/>
      <rect x="23" y="543" width="739" height="2"/>
      <rect x="23" y="598.9" width="739" height="2"/>
      <rect x="23" y="651" width="739" height="2"/>
      <rect x="23" y="757.2" width="739" height="2"/>
      <rect x="23" y="785.8" width="739" height="2"/>
    </g>
    <polygon fill="var(--band-gray)" points="42,1055 290,1055 245,1101 7,1101"/>
    <polygon fill="var(--ink)" points="301,1030 786,1030 786,1101 245,1101"/>
    <polygon fill="var(--paper)" points="477,1042 786,1042 786,1050 470,1050"/>
  </svg>

  <div class="brand">
    <span class="brand-dot"></span>
    <span class="brand-name">Silver Lumen<br>Med Spa</span>
  </div>

  <h1 class="title"><span>Ageless Glow</span><br><span class="line-two">Memberships</span></h1>

  <div class="col-head treatments">Trreatments</div>
  <div class="col-head tier good">Good</div>
  <div class="col-head tier better">Better</div>
  <div class="col-head tier best">Best</div>

  <div class="price-row">
    <div class="label">Green Unlimited/<br>Choose one color per month</div>
    <div class="price good">$189</div>
    <div class="price better">$289</div>
    <div class="price best">$389</div>
  </div>

  <div class="row" style="top:248px"><span class="name">Skin Evaluation</span><span class="cell good"><svg><use href="#tick"/></svg></span><span class="cell better"><svg><use href="#tick"/></svg></span><span class="cell best"><svg><use href="#tick"/></svg></span></div>
  <div class="row" style="top:274px"><span class="name">Infrared Sauna</span><span class="cell good"><svg><use href="#tick"/></svg></span><span class="cell better"><svg><use href="#tick"/></svg></span><span class="cell best"><svg><use href="#tick"/></svg></span></div>
  <div class="row" style="top:300px"><span class="name">Massage Chair</span><span class="cell good"><svg><use href="#tick"/></svg></span><span class="cell better"><svg><use href="#tick"/></svg></span><span class="cell best"><svg><use href="#tick"/></svg></span></div>
  <div class="row end" style="top:325px"><span class="name">Vibrational Lymphatic Plate</span><span class="cell good"><svg><use href="#tick"/></svg></span><span class="cell better"><svg><use href="#tick"/></svg></span><span class="cell best"><svg><use href="#tick"/></svg></span></div>

  <div class="row" style="top:355px"><span class="name">Medical Facial</span><span class="cell good"><svg><use href="#tick"/></svg></span><span class="cell better"><svg><use href="#tick"/></svg></span><span class="cell best"><svg><use href="#tick"/></svg></span></div>
  <div class="row" style="top:380px"><span class="name">Face Lymphatic Drainage</span><span class="cell good"><svg><use href="#tick"/></svg></span><span class="cell better"><svg><use href="#tick"/></svg></span><span class="cell best"><svg><use href="#tick"/></svg></span></div>
  <div class="row" style="top:407px"><span class="name">Red Light Therapy</span><span class="cell good"><svg><use href="#tick"/></svg></span><span class="cell better"><svg><use href="#tick"/></svg></span><span class="cell best"><svg><use href="#tick"/></svg></span></div>
  <div class="row end" style="top:432px"><span class="name">Ph Oxygen Serum</span><span class="cell good"><svg><use href="#tick"/></svg></span><span class="cell better"><svg><use href="#tick"/></svg></span><span class="cell best"><svg><use href="#tick"/></svg></span></div>

  <div class="row end" style="top:461px"><span class="name">Chemical Peels Progressive or Middepth</span><span class="cell good"><svg><use href="#tick"/></svg></span><span class="cell better"><svg><use href="#tick"/></svg></span><span class="cell best"><svg><use href="#tick"/></svg></span></div>

  <div class="row" style="top:491px"><span class="name">Halcyon Broadband Ageless Glow</span><span class="cell good"><svg><use href="#tick"/></svg></span><span class="cell better"><svg><use href="#tick"/></svg></span><span class="cell best"><svg><use href="#tick"/></svg></span></div>
  <div class="row end" style="top:517px"><span class="name">Halcyon 2 Correction Passes</span><span class="cell good"><svg><use href="#tick"/></svg></span><span class="cell better"><svg><use href="#tick"/></svg></span><span class="cell best"><svg><use href="#tick"/></svg></span></div>

  <div class="row" style="top:546px"><span class="name">Dermaplaning</span><span class="cell better"><svg><use href="#tick"/></svg></span><span class="cell best"><svg><use href="#tick"/></svg></span></div>
  <div class="row end" style="top:571px"><span class="name">Vitamin A Peel</span><span class="cell better"><svg><use href="#tick"/></svg></span><span class="cell best"><svg><use href="#tick"/></svg></span></div>

  <div class="row" style="top:600px"><span class="name">Halcyon Upto 10 Correction Passes</span><span class="cell better"><svg><use href="#tick"/></svg></span><span class="cell best"><svg><use href="#tick"/></svg></span></div>
  <div class="row end" style="top:625px"><span class="name">Halcyon Hair Removal</span><span class="cell better"><svg><use href="#tick"/></svg></span><span class="cell best"><svg><use href="#tick"/></svg></span></div>

  <div class="row" style="top:653px"><span class="name">Microneedling</span><span class="cell better"><svg><use href="#tick"/></svg></span><span class="cell best"><svg><use href="#tick"/></svg></span></div>
  <div class="row" style="top:679px"><span class="name">Halcyon Firm Tone</span><span class="cell best"><svg><use href="#tick"/></svg></span></div>
  <div class="row" style="top:705px"><span class="name">Microneedling Thread Afterlux</span><span class="cell best"><svg><use href="#tick"/></svg></span></div>
  <div class="row end" style="top:730px"><span class="name">Chemical Peel Velia Italian</span><span class="cell best"><svg><use href="#tick"/></svg></span></div>

  <div class="row end" style="top:760px"><span class="name">Contoura Targeted Weight Loss</span><span class="cell best"><svg><use href="#tick"/></svg></span></div>

  <div class="row" style="top:788px"><span class="name">Laser Rejuvenation</span><span class="cell good">10% Off</span><span class="cell better">20% Off</span><span class="cell best">30% Off</span></div>
  <div class="row" style="top:814px"><span class="name">Plasma Pen</span><span class="cell good">10% Off</span><span class="cell better">20% Off</span><span class="cell best">30% Off</span></div>
  <div class="row" style="top:839px"><span class="name">Hyperbaric Oxygen</span><span class="cell good">10% Off</span><span class="cell better">20% Off</span><span class="cell best">30% Off</span></div>
  <div class="row" style="top:865px"><span class="name">Massage</span><span class="cell good">10% Off</span><span class="cell better">20% Off</span><span class="cell best">30% Off</span></div>
  <div class="row" style="top:891px"><span class="name">Airbrush Tanning</span><span class="cell good">10% Off</span><span class="cell better">20% Off</span><span class="cell best">30% Off</span></div>
  <div class="row" style="top:916px"><span class="name">Ionic Detox</span><span class="cell good">10% Off</span><span class="cell better">20% Off</span><span class="cell best">30% Off</span></div>
  <div class="row" style="top:942px"><span class="name">Lymphatic Drainage</span><span class="cell good">10% Off</span><span class="cell better">20% Off</span><span class="cell best">30% Off</span></div>
  <div class="row" style="top:967px"><span class="name">Tirzepatide Weight Loss Peptide</span><span class="cell good">10% Off</span><span class="cell better">20% Off</span><span class="cell best">30% Off</span></div>
  <div class="row end" style="top:993px"><span class="name">Lip Fillers Neddle-less</span><span class="cell good">10% Off</span><span class="cell better">20% Off</span><span class="cell best">30% Off</span></div>

  <div class="footer-item web">
    <svg viewBox="0 0 20 20"><g fill="none" stroke="#f2f2f2" stroke-width="1"><circle cx="10" cy="10" r="9.3"/><circle cx="10" cy="10" r="5.5"/><ellipse cx="10" cy="10" rx="2.4" ry="5.5"/><path d="M4.5 10h11M5.3 7.5h9.4M5.3 12.5h9.4"/></g></svg>
    <span>SilverLumenMedSpa.com</span>
  </div>
  <div class="footer-item phone">
    <svg viewBox="0 0 20 20"><g fill="none" stroke="#fff" stroke-width="1"><circle cx="10" cy="10" r="9.3"/><path d="M7.2 5.3l1.4 2.3-1 1.1c.6 1.3 1.6 2.3 2.9 2.9l1.1-1 2.3 1.4-.7 1.9c-3.6-.1-6.8-3.3-7-7z"/><path d="M11 5.2a4 4 0 0 1 3.8 3.8M11 7a2.2 2.2 0 0 1 2 2"/></g></svg>
    <span>214.555.0148</span>
  </div>
  <div class="footer-item place">
    <svg viewBox="0 0 20 20"><g fill="none" stroke="#fff" stroke-width="1"><circle cx="10" cy="10" r="9.3"/><path d="M10 15.2s-3.6-3.9-3.6-6.5a3.6 3.6 0 0 1 7.2 0c0 2.6-3.6 6.5-3.6 6.5z"/><circle cx="10" cy="8.7" r="1.4"/></g></svg>
    <span>1180 Harlow Ave. Brookmere, Tx 75990</span>
  </div>
</main>
</body>
</html>
```